Magazine Cover & Back, Course Overview

Please read this whole description and follow directions before proceeding. Please do not submit multiple designs that look similar. If you submit multiple designs that look similar you will be disqualified and receive a poor rating. A magazine design includes a cover and back. This is a single design and should be submitted as such. Do not submit one design for the front only, then a separate design for the back, then a third mock up. Submit all as a single design. I need a magazine cover and back. The size will be standard paper size, 8-1/2" x 11". It will be used for a course overview, a summary of a boating instruction course. I have attached examples and pictures that can be used. I have also attached required content. The final designs must NOT be AI files. Text must be editable with Adobe Acrobat DC.

Target Market(s)

Military & Government

Industry/Entity Type

Military & Government

Requirements
Must have
• See attached.
Nice to have
• See attached.
Should not have
• See attached.

```html
<!DOCTYPE html>
<html lang="en">
<head>
<meta charset="utf-8">
<title>Diver Support Vessel Training – Course Overview</title>
<link rel="stylesheet" href="https://fonts.googleapis.com/css2?family=Jost:wght@300;400;600;700&display=swap">
<style>
  :root {
    --brand-blue: #0aaeea;
    --paper: #ffffff;
    --ink: #1b1b1b;
    --logo-grey: #4a4a4a;
    --trim: #555555;
    --sky: #4f9fe0;
    --hull: #9a9a94;
    --water: #6f767a;
  }
  html, body {
    margin: 0;
    width: 851px;
    height: 1200px;
    overflow: hidden;
    background: var(--paper);
  }
  .spread {
    position: absolute;
    left: 20px;
    top: 338px;
    width: 811px;
    height: 524px;
    font-family: "Jost", sans-serif;
  }
  .blue { fill: var(--brand-blue); }
  .paper { fill: var(--paper); }
  .trim { fill: none; stroke: var(--trim); stroke-width: 1; }
  .fold { stroke: #9ab; stroke-width: 1; }
  .title-main { font-weight: 700; font-size: 66px; fill: var(--paper); letter-spacing: 1px; }
  .title-sub { font-weight: 700; font-size: 24px; fill: var(--paper); letter-spacing: 0.5px; }
  .title-light { font-weight: 300; font-size: 42px; fill: var(--paper); letter-spacing: 3px; }
  .point-head { font-weight: 700; font-size: 19px; fill: var(--ink); }
  .point-body { font-weight: 400; font-size: 18px; fill: var(--ink); }
  .bullet { fill: var(--brand-blue); }
  .badge { fill: var(--logo-grey); }
  .company-name { font-weight: 400; font-size: 28px; fill: var(--logo-grey); }
  .company-line { font-weight: 400; font-size: 11px; fill: var(--logo-grey); letter-spacing: 1.2px; }
</style>
</head>
<body>
<svg class="spread" viewBox="0 0 1181 763" xmlns="http://www.w3.org/2000/svg">
  <defs>
    <linearGradient id="vesselPhoto" x1="0" y1="0" x2="0" y2="1">
      <stop offset="0" stop-color="#3f8fd8"/>
      <stop offset="0.45" stop-color="#6aa8e0"/>
      <stop offset="0.55" stop-color="#5a4a3e"/>
      <stop offset="0.7" stop-color="#b8b8b2"/>
      <stop offset="1" stop-color="#8d8d88"/>
    </linearGradient>
    <linearGradient id="consolePhoto" x1="0" y1="0" x2="1" y2="1">
      <stop offset="0" stop-color="#7b7e74"/>
      <stop offset="1" stop-color="#2f3236"/>
    </linearGradient>
    <linearGradient id="deckPhoto" x1="0" y1="0" x2="1" y2="1">
      <stop offset="0" stop-color="#5e676c"/>
      <stop offset="1" stop-color="#a7a9a6"/>
    </linearGradient>
    <clipPath id="frontPage"><rect x="605" y="0" width="576" height="763"/></clipPath>
  </defs>

  <!-- back cover -->
  <g class="back-cover">
    <rect class="paper" x="0" y="0" width="605" height="763"/>
    <polygon class="blue" points="295,0 605,0 605,763 295,763 295,586 571,310"/>
    <polygon class="paper" points="295,478 421,590 295,704 178,590"/>
    <polygon role="img" aria-label="Photo: coxswain's hands at a deck winch control over the water" fill="url(#deckPhoto)" points="295,495 391,590 295,686 200,590"/>

    <g class="course-points">
      <polygon class="bullet" points="75,162 85,172 75,182 65,172"/>
      <text class="point-head" x="90" y="169">To assist Navy Sailors with</text>
      <text class="point-body" x="90" y="190">Becoming More Proficient Coxswains</text>

      <polygon class="bullet" points="75,223 85,233 75,243 65,233"/>
      <text class="point-head" x="90" y="230">Focused on</text>
      <text class="point-body" x="90" y="251">Safety &amp; Close-Quarters Maneuvering</text>

      <polygon class="bullet" points="75,286 85,296 75,306 65,296"/>
      <text class="point-head" x="90" y="291">Custom Made Course for</text>
      <text class="point-body" x="90" y="312">Specific Users, Scenarios and Vessels</text>
      <text class="point-body" x="90" y="332">Based on OIC Involvement,</text>
      <text class="point-body" x="90" y="352">Client Feedback and After Action Reviews</text>

      <polygon class="bullet" points="75,385 85,395 75,405 65,395"/>
      <text class="point-head" x="90" y="393">Taught by</text>
      <text class="point-body" x="90" y="413">Reputable USCG Licensed Boat Captains</text>

      <polygon class="bullet" points="75,436 85,446 75,456 65,446"/>
      <text class="point-head" x="90" y="453">Includes Useful Aids</text>
    </g>
  </g>

  <!-- front cover -->
  <g class="front-cover">
    <rect class="blue" x="605" y="0" width="576" height="763"/>
    <g clip-path="url(#frontPage)">
      <polygon class="paper" points="1009,0 1317,306 1011,612 705,306"/>
      <polygon class="paper" points="868,763 868,680 1011,560 1181,560 1181,763"/>
      <polygon class="paper" points="1009,0 1181,0 1181,200"/>
      <polygon role="img" aria-label="Photo: diver support vessel underway with the US flag flying" fill="url(#vesselPhoto)" points="1011,26 1291,306 1011,586 731,306"/>
      <polygon class="blue" points="876,417 1006,547 876,677 746,547"/>
      <polygon role="img" aria-label="Photo: helm console with crew training aboard" fill="url(#consolePhoto)" points="877,429 995,547 877,665 759,547"/>
    </g>

    <g class="cover-title">
      <text class="title-main" x="633" y="103">DIVER</text>
      <text class="title-sub" x="633" y="129">SUPPORT VESSEL</text>
      <text class="title-light" x="633" y="166">TRAINING</text>
    </g>

    <circle class="badge" cx="1102" cy="608" r="32"/>

    <g class="company-mark">
      <circle class="badge" cx="955" cy="690" r="12"/>
      <text class="company-name" x="975" y="698">Harborline</text>
      <text class="company-line" x="975" y="718">MARINE SERVICES, LLC</text>
    </g>
  </g>

  <line class="fold" x1="605" y1="0" x2="605" y2="763"/>
  <rect class="trim" x="0.5" y="0.5" width="1180" height="762"/>
</svg>
</body>
</html>
```